Stationery Design Project - Mark Delaveri

I have recently designed my personal logo - Mark Delaveri (here on pixelhive.com) and now i'm looking to complete my corporate identity, with adding:
- Business Card
- Letter Head
- Envelope
- Brochure template (that will be used to promote any of the workshops or other services I provide along with a short summary about my credentials, and testimonials) - you can take your pick from the website: http://markdelaveri.com

Refer to website for more insight into the brand and the look & feel

PS.
- PLEASE REFER TO ATTACHED FILE AND READ THE "SHOULD NOT HAVE SECTION OF THIS BRIEF"
- I have attached two vector files, displaying the logo alteration on two different backgrounds (dark & light)
Updates

ONLY 2 DAYS LEFT ON DEADLINE. KEEP THOSE DESIGNS COMING.

Target Market(s)

1) One-on-one Business Executive 2) Companies requesting my workshops for mid management teams & public speaking events like BRIM Forums

Industry/Entity Type

Business

Requirements
Must have
• - must fit the look and feel of the logo (notice that I have attached the logo, and an emblem)
- the final files should be ready for printing - with info on colours, sizes, bleed area, margins, UV spot (if applicable), suggested material to print on (applies to business cards in particular)
- brand guide lines should be laid out too (font, colour, etc ...)
Nice to have
• It would be nice to produce something different that your standard sizes & di-cut in terms of business card, and letter head ...
Should not have
• THE EMBLEM (MD) AND THE LOGO (MARK DELAVERI) SHOULD NOT BE LAYED OUT AS PER THE ATTACHED FILE - THEY SHOULD BE SEPARATED - THE EMBLEM (MD) CAN BE USED IN PARTIAL OR AS WATERMARK - BUT NOT THE LOGO (MARK DELAVERI)

```html
<!DOCTYPE html>
<html lang="en">
<head>
<meta charset="utf-8">
<title>Mark Delaveri — Bifold Brochure, Outside Face</title>
<link rel="stylesheet" href="https://fonts.googleapis.com/css2?family=Fjalla+One&family=Open+Sans:wght@400;600&family=Arimo:wght@400;700&display=swap">
<style>
  :root{
    --ink:#222120;
    --sky:#62bae3;
    --sky-deep:#4a86c5;
    --slate:#7a7a7a;
    --paper-a:#f4f2f1;
    --paper-b:#e7e2e1;
    --bleed:#d9d6d4;
    --sand:#d9d2c8;
    --white:#ffffff;
    --trim:#d0282c;
    --safe:#1e9fd6;
    --label:#444444;
    --map-a:#6f7a63;
    --map-b:#a59a86;
    --photo-a:#c9c4c0;
    --photo-b:#6d6762;
  }
  html,body{margin:0;padding:0;overflow:hidden;background:#fff;}
  .canvas{width:1200px;height:955px;position:relative;overflow:hidden;}
  .canvas svg{display:block;}
  .head-label{font-family:"Arimo",sans-serif;font-weight:700;fill:var(--label);}
  .head-title{font-size:20px;}
  .head-sub{font-size:14px;fill:#666;}
  .dim{font-family:"Arimo",sans-serif;font-size:13px;fill:#333;}
  .dim-line{stroke:var(--safe);stroke-width:1.2;}
  .note-title{font-family:"Arimo",sans-serif;font-size:13px;}
  .note-body{font-family:"Arimo",sans-serif;font-size:10px;fill:#444;}
  .spec-key{font-family:"Arimo",sans-serif;font-size:10px;font-weight:700;fill:#222;}
  .spec-val{font-family:"Arimo",sans-serif;font-size:10px;fill:#444;}
  .condensed{font-family:"Fjalla One",sans-serif;}
  .body-copy{font-family:"Open Sans",sans-serif;font-size:12.5px;fill:var(--white);}
  .print-note{font-family:"Arimo",sans-serif;font-weight:700;font-size:14px;fill:var(--trim);}
</style>
</head>
<body>
<main class="canvas">
<svg width="1200" height="955" viewBox="0 0 1200 955" xmlns="http://www.w3.org/2000/svg">
  <defs>
    <linearGradient id="paper" x1="0" y1="0" x2="1" y2="1">
      <stop offset="0" stop-color="var(--paper-a)"/>
      <stop offset="1" stop-color="var(--paper-b)"/>
    </linearGradient>
    <linearGradient id="mapTone" x1="0" y1="0" x2="1" y2="1">
      <stop offset="0" stop-color="var(--map-b)"/>
      <stop offset="1" stop-color="var(--map-a)"/>
    </linearGradient>
    <linearGradient id="photoTone" x1="0" y1="0" x2="1" y2="1">
      <stop offset="0" stop-color="var(--photo-a)"/>
      <stop offset="1" stop-color="var(--photo-b)"/>
    </linearGradient>
  </defs>

  <!-- panel headings -->
  <g class="panel-headings">
    <text class="head-label head-title" x="268" y="18" text-anchor="middle">BACK COVER</text>
    <text class="head-label head-sub" x="268" y="35" text-anchor="middle">LEFT PANEL</text>
    <text class="head-label head-title" x="770" y="18" text-anchor="middle">FRONT COVER</text>
    <text class="head-label head-sub" x="770" y="35" text-anchor="middle">RIGHT PANEL</text>
  </g>

  <!-- dimension lines -->
  <g class="dimensions">
    <line class="dim-line" x1="10" y1="72" x2="230" y2="72"/>
    <line class="dim-line" x1="308" y1="72" x2="732" y2="72"/>
    <line class="dim-line" x1="812" y1="72" x2="1008" y2="72"/>
    <line x1="10" y1="66" x2="16" y2="78" stroke="#555"/>
    <line x1="504" y1="66" x2="514" y2="78" stroke="#555"/>
    <line x1="1002" y1="66" x2="1010" y2="78" stroke="#555"/>
    <text class="dim" x="268" y="77" text-anchor="middle">5.5"</text>
    <text class="dim" x="772" y="77" text-anchor="middle">5.5"</text>
  </g>

  <!-- artboard -->
  <rect class="bleed-area" x="4" y="95" width="1013" height="788" fill="var(--bleed)"/>
  <rect class="front-paper" x="4" y="95" width="1002" height="788" fill="url(#paper)"/>

  <!-- dark geometry -->
  <polygon class="back-dark" points="4,95 218,95 509,388 268,630 510,872 508,883 4,883" fill="var(--ink)"/>
  <polygon class="front-dark" points="750,630 1006,883 508,883 510,872" fill="var(--ink)"/>

  <!-- blue diamond with photo -->
  <polygon class="accent-diamond" points="509,388 750,630 510,872 268,630" fill="var(--sky)"/>
  <polygon class="photo-slot" role="img" aria-label="Photo of a professional working at a desk in an office" points="388,510 508,630 390,750 268,630" fill="url(#photoTone)"/>
  <polygon class="map-strip" role="img" aria-label="Aerial map view of the office location" points="4,365 268,630 22,876 4,876" fill="url(#mapTone)"/>

  <text font-size="34" fill="var(--ink)" transform="translate(548,690) rotate(-55)" text-anchor="middle" style="font-family:'Open Sans',sans-serif">Image space</text>

  <!-- back cover content -->
  <g class="back-brand">
    <circle cx="80" cy="268" r="22" fill="var(--white)"/>
    <text class="condensed" x="114" y="283" font-size="42" fill="var(--white)">MD</text>
  </g>
  <g class="contact">
    <polygon points="53,369 75,369 64,378" fill="#8a8a8a"/>
    <text class="condensed" x="88" y="398" font-size="38" fill="var(--sand)">ADDRESS</text>
    <text class="condensed" x="117" y="430" font-size="22" fill="var(--sand)">LOREM IPSUM 0551 AMET</text>
    <text class="condensed" x="147" y="460" font-size="22" fill="var(--sand)">+41 58 21 93 07</text>
    <text class="condensed" x="177" y="490" font-size="20" fill="#9a9a9a">INFO@DELAVERIGROUP.NY</text>
  </g>
  <polygon points="331,730 346,745 331,745" fill="#8a8a8a"/>
  <g class="body-copy back-copy" text-anchor="start">
    <text x="190" y="766" textLength="168" lengthAdjust="spacingAndGlyphs">Lorem ipsum dolor sit amet,</text>
    <text x="170" y="786" textLength="210" lengthAdjust="spacingAndGlyphs">consectetur adipisicing elit, sed do</text>
    <text x="162" y="806" textLength="239" lengthAdjust="spacingAndGlyphs">eiusmod tempor incididunt ut labore et</text>
    <text x="292" y="827" textLength="128" lengthAdjust="spacingAndGlyphs">dolore magna aliqua.</text>
  </g>

  <!-- front cover content -->
  <g class="front-brand">
    <circle cx="795" cy="343" r="44" fill="#555"/>
    <text class="condensed" x="795" y="448" font-size="54" fill="#5a5a5a" text-anchor="middle">MARK DELAVERI</text>
    <text class="condensed" x="860" y="516" font-size="50" fill="var(--slate)" text-anchor="middle">BROCHURE</text>
    <text x="868" y="542" font-size="13" fill="var(--sky-deep)" text-anchor="middle" style="font-family:'Open Sans',sans-serif">Lorem ipsum dolor sit amet</text>
  </g>
  <g class="body-copy front-copy" text-anchor="start">
    <text x="676" y="766" textLength="172" lengthAdjust="spacingAndGlyphs">Lorem ipsum dolor sit amet,</text>
    <text x="656" y="786" textLength="212" lengthAdjust="spacingAndGlyphs">consectetur adipisicing elit, sed do</text>
  </g>
  <text class="condensed" x="750" y="833" font-size="13" fill="#8a8a8a" text-anchor="middle" letter-spacing="0.5">LOREM IPSUM DOLOR SIT AMET, CONSECTETUR ADIPISICING ELIT.</text>

  <!-- print guides -->
  <rect class="trim-guide" x="11" y="102" width="998" height="774" fill="none" stroke="var(--trim)" stroke-width="1" stroke-dasharray="2 3"/>
  <rect class="safe-guide" x="27" y="118" width="967" height="742" fill="none" stroke="var(--safe)" stroke-width="1" stroke-dasharray="2 3"/>

  <!-- guide notes -->
  <g class="guide-notes">
    <line x1="1012" y1="130" x2="1022" y2="138" stroke="#000"/>
    <line x1="1022" y1="138" x2="1170" y2="138" stroke="#000"/>
    <text class="note-title" x="1127" y="130" fill="#000">BLEED</text>

    <line x1="1012" y1="168" x2="1170" y2="168" stroke="var(--trim)"/>
    <text class="note-title" x="1091" y="165" fill="var(--trim)">TRIM</text>
    <g stroke="var(--trim)" stroke-width="1.4" fill="none">
      <circle cx="1002" cy="176" r="3"/><circle cx="1009" cy="176" r="3"/>
      <line x1="1002" y1="173" x2="1009" y2="158"/><line x1="1009" y1="173" x2="1002" y2="158"/>
    </g>
    <text class="note-body" x="1093" y="183">This is the actual cut of</text>
    <text class="note-body" x="1093" y="197">the final design.</text>

    <line x1="990" y1="252" x2="1000" y2="245" stroke="var(--safe)"/>
    <line x1="1000" y1="250" x2="1170" y2="250" stroke="var(--safe)"/>
    <text class="note-title" x="1041" y="247" fill="var(--safe)">SAFE ZONE</text>
    <text class="note-body" x="1041" y="268">DO NOT place important texts or</text>
    <text class="note-body" x="1041" y="283">images beyond the dotted area to</text>
    <text class="note-body" x="1041" y="298">prevent trimming.</text>
  </g>

  <!-- spec sheet -->
  <g class="specs">
    <text class="spec-key" x="1041" y="355">Size</text><text class="spec-val" x="1086" y="355">11 x 8.5 in</text>
    <text class="spec-key" x="1041" y="370">Side</text><text class="spec-val" x="1086" y="370">Front (Outside Face)</text>
    <text class="spec-key" x="1041" y="385">Fold</text><text class="spec-val" x="1086" y="385">Bifold</text>
    <text class="spec-key" x="1041" y="416">Colors</text>
    <polygon points="1085,410 1092,398 1106,398 1113,410 1106,422 1092,422" fill="var(--sky)"/>
    <polygon points="1108,424 1115,412 1129,412 1136,424 1129,436 1115,436" fill="var(--sky-deep)"/>
    <polygon points="1085,438 1092,426 1106,426 1113,438 1106,450 1092,450" fill="var(--slate)"/>
    <polygon points="1108,452 1115,440 1129,440 1136,452 1129,464 1115,464" fill="var(--ink)"/>
  </g>

  <text class="print-note" x="510" y="930" text-anchor="middle">REMOVE THIS LAYER</text>
  <text class="print-note" x="512" y="948" text-anchor="middle">BEFORE PRINTING THIS FILE</text>
</svg>
</main>
</body>
</html>
```